Modern solo law firm website

I am preparing to launch a solo law practice (I own the domain farrowcounsel.com and/or may use Farrow Law Office as a dba), and will need to move quickly to put up a website once I pull the trigger. There are many existing law firm sites to "copy," but I'm looking for something a little more modern and unique with some scrolling and modern icons (see e.g., brintelaw.com). Right now, need the logo and skeleton for the site, as I have not written all of the content. For now, I like the idea of a simple home page that incorporates the phrase "Impactful. Valuable. Trusted." (Again, I may change that text.) And would like links on the home page across the top for "about", "services", "people" and "contact" -- these should lead to separate landing pages. The bottom of the home page also should have a link for a "disclaimer" and to Facebook, Twitter and LinkedIn (which I have not yet created). Make sense? Let me know if you have questions.

Target Market(s)

Business clients

Industry/Entity Type

Law Firm

Number of Pages Required

5+ page

Font styles to use
Other font styles liked:
• Perhaps Segoe UI

Requirements
Must have
• DRAFT STRUCTURE AND TEXT NOW ATTACHED. HOWEVER, SUBJECT TO EDITS BEING MADE CONCURRENTLY.

```html
<!DOCTYPE html>
<html lang="en">
<head>
<meta charset="utf-8">
<title>Farrow Counsel</title>
<link rel="stylesheet" href="https://fonts.googleapis.com/css2?family=Open+Sans:wght@400;600&family=Arimo:wght@400&display=swap">
<style>
  :root {
    --brand-blue: #1f72b8;
    --nav-grey: #5a5a5a;
    --social-blue: #1a9ad6;
    --hero-deep: #1a6fc4;
    --hero-light: #4fb2f0;
    --intro-bg: #eeecf2;
    --intro-text: #176a93;
    --services-bg: #2a6f86;
    --services-deep: #1f5d73;
    --icon-fill: #4d8fa1;
    --white: #ffffff;
    --footer-bg: #03283d;
    --footer-logo: #b9d4e0;
    --button-bg: #4f93a4;
  }
  * { box-sizing: border-box; margin: 0; padding: 0; }
  html, body { width: 1092px; height: 1200px; overflow: hidden; }
  body { font-family: "Open Sans", "Segoe UI", sans-serif; background: var(--white); }

  .site-header {
    height: 79px;
    background: linear-gradient(#ffffff, #e6e6e6);
    display: flex; align-items: center;
    padding: 0 91px;
    border-bottom: 1px solid #d6d6d6;
  }
  .brand { font-size: 32px; font-weight: 400; color: var(--brand-blue); letter-spacing: -0.3px; }
  .main-nav { margin-left: auto; display: flex; gap: 32px; font-size: 15px; color: var(--nav-grey); }
  .social { display: flex; gap: 4px; margin-left: 33px; }
  .social span { width: 20px; height: 20px; background: var(--social-blue); display: block; }

  .hero {
    position: relative; height: 467px;
    background:
      radial-gradient(circle at 23% 36%, rgba(255,230,240,0.75) 0, rgba(255,255,255,0) 9%),
      radial-gradient(ellipse at 78% 60%, rgba(140,220,240,0.55) 0, rgba(80,160,220,0) 45%),
      radial-gradient(circle at 40% 78%, rgba(120,200,255,0.5) 0, rgba(120,200,255,0) 14%),
      linear-gradient(110deg, var(--hero-light) 0%, var(--hero-deep) 45%, #3b8fcf 75%, #2a6aa8 100%);
    color: var(--white);
  }
  .hero-title {
    position: absolute; left: 93px; top: 161px;
    font-size: 58px; font-weight: 600; line-height: 78px;
    color: rgba(225,240,255,0.85);
  }
  .hero-sub { position: absolute; left: 94px; top: 400px; font-size: 22px; font-weight: 400; }

  .intro {
    height: 270px; text-align: center; color: var(--intro-text);
    background:
      radial-gradient(ellipse at 15% 40%, rgba(200,195,230,0.6), rgba(238,236,242,0) 30%),
      radial-gradient(ellipse at 85% 55%, rgba(200,195,230,0.6), rgba(238,236,242,0) 30%),
      var(--intro-bg);
    padding: 36px 100px 0;
  }
  .intro h2 { font-size: 29px; font-weight: 600; color: #1d6a92; margin-bottom: 16px; }
  .intro p { font-size: 12.6px; line-height: 18px; margin-bottom: 5px; }

  .services {
    height: 296px;
    background: radial-gradient(ellipse at 55% 80%, #35879c, var(--services-bg) 45%, var(--services-deep));
    display: grid; grid-template-columns: 246px 238px 238px 238px;
    padding: 31px 0 0 52px;
    color: var(--white); text-align: center;
  }
  .service-icon {
    width: 66px; height: 66px; border-radius: 50%;
    border: 2px solid var(--white); background: var(--icon-fill);
    margin: 0 auto 16px; display: flex; align-items: center; justify-content: center;
  }
  .service h3 { font-size: 16px; font-weight: 400; color: #0f1f28; margin-bottom: 7px; white-space: nowrap; }
  .service p { font-family: "Arimo", Arial, sans-serif; font-size: 11px; line-height: 15.5px; width: 192px; margin: 0 auto; letter-spacing: 0.2px; }
  .service:nth-child(2) p { width: 198px; }
  .service:nth-child(4) p { width: 210px; }

  .site-footer {
    height: 88px; background: var(--footer-bg); border-top: 2px solid #6fa3b6;
    display: flex; align-items: flex-start; padding: 22px 0 0 93px; color: var(--white);
  }
  .footer-brand { font-size: 22px; color: var(--footer-logo); width: 292px; margin-top: 3px; }
  .footer-address { font-size: 12.6px; line-height: 20px; width: 108px; }
  .footer-contact { font-size: 12.6px; line-height: 20px; width: 253px; margin-top: -2px; }
  .cta {
    margin-top: 7px; width: 217px; height: 31px; border-radius: 16px;
    background: var(--button-bg); border: 2px solid #b7d7e0;
    color: var(--white); font-size: 16px; text-align: center; line-height: 27px;
  }
</style>
</head>
<body>
  <header class="site-header">
    <div class="brand">Farrowcounsel</div>
    <nav class="main-nav">
      <span>about</span><span>services</span><span>people</span><span>contact</span>
    </nav>
    <div class="social" aria-label="Social links">
      <span role="img" aria-label="Social link one"></span>
      <span role="img" aria-label="Social link two"></span>
      <span role="img" aria-label="Social link three"></span>
    </div>
  </header>

  <section class="hero" role="img" aria-label="Blue photo of a globe with scales of justice and lens flare">
    <h1 class="hero-title">Impactful.<br>Valuable. Trusted.</h1>
    <p class="hero-sub">Big Law plays an important part in the legal services industry</p>
  </section>

  <section class="intro">
    <h2>Impactful. Valuable. Trusted.</h2>
    <p>That’s how you should think of your lawyers, right?</p>
    <p>Big Law plays an important part in the legal services industry. While you get the resources of a large organization, the services are costly and mis-incentivized so your lawyers benefit from taking longer and chasing every angle, regardless of whether it makes the most sense for your needs and budget. Been there, seen that.</p>
    <p>Farrow Counsel is committed to making your life easier. To explore and listen to your true needs. To provide simple explanations that enable you to make the right business decisions. Farrow Counsel is fully committed to providing high-impact work at an unquestionable value to help youachieve great success. And to earning your unwavering trust for the long haul.</p>
  </section>

  <section class="services">
    <article class="service">
      <div class="service-icon">
        <svg width="30" height="24" viewBox="0 0 30 24" fill="none" stroke="#fff" stroke-width="1.3">
          <rect x="14" y="1" width="10" height="5"/><rect x="8" y="9" width="10" height="5" fill="#fff"/><rect x="2" y="17" width="10" height="5"/><rect x="16" y="17" width="10" height="5" fill="#fff"/>
        </svg>
      </div>
      <h3>Outside general counsel.</h3>
      <p>Maybe you have an in-house counsel, or maybe you don't. Farrow Counsel can provide you with the in-house counsel services your company needs so your employees can focus on their primary jobs.</p>
    </article>
    <article class="service">
      <div class="service-icon">
        <svg width="20" height="26" viewBox="0 0 20 26" fill="none" stroke="#fff" stroke-width="1.5">
          <path d="M2 1h16M2 25h16M4 1c0 8 12 8 12 12S4 17 4 25M16 1c0 8-12 8-12 12s12 4 12 12"/><path d="M7 22l3-5 3 5z" fill="#fff"/>
        </svg>
      </div>
      <h3>Litigation and dispute resolution.</h3>
      <p>Business disputes can be very expensive and disruptive. Farrow Counsel canvigorously fight to resolve business disputes favorably, and more importantly help you anticipate problems at the outset to prevent them in the future.</p>
    </article>
    <article class="service">
      <div class="service-icon">
        <svg width="28" height="24" viewBox="0 0 28 24" fill="#fff">
          <path d="M4 6h16V2l7 6-7 6v-4H4z"/><path d="M24 14H8v-4l-7 6 7 6v-4h16z"/>
        </svg>
      </div>
      <h3>Employment consulting.</h3>
      <p>Hiring, NDAs and non-compete agreements, policies and handbooks, separations, disputes. Farrow Counsel has experience counseling to avoid employment issues and in problem solving and working them out.</p>
    </article>
    <article class="service">
      <div class="service-icon">
        <svg width="32" height="32" viewBox="0 0 32 32" fill="none" stroke="#fff" stroke-width="1.2">
          <rect x="2" y="12" width="8" height="18"/><rect x="11" y="3" width="10" height="27"/><rect x="22" y="9" width="8" height="21"/>
          <path d="M14 8v2M18 8v2M14 14v2M18 14v2M5 17v2M25 14v2M26 20v2M14 20v2"/>
        </svg>
      </div>
      <h3>Business documents.</h3>
      <p>Why frown about creating a new agreement or sweat over what someone else may be slipping into their form? Farrow Counsel is experienced in drafting, reviewing and negotiating many types of business agreements, including real estate agreements and leases, business organizationdocuments, and commercial contracts of many kinds.</p>
    </article>
  </section>

  <footer class="site-footer">
    <div class="footer-brand">Farrowcounsel</div>
    <div class="footer-address">Farrow Counsel<br>418 Alder Lane</div>
    <div class="footer-contact">Northfield, IL60093<br>555-014-2287<br>info@farrowcounsel.com</div>
    <div class="cta">Get in Touch</div>
  </footer>
</body>
</html>
```